Business cards, envelopes, etc. for real estate company

We have a finished logo for our real estate company. We need a corporate identity package with the following items:

1. Business Cards
2. Letterhead/Stationary - with 2 pages:
-1st page with full header
-2nd page without top header
3. Concise and professional e-mail signature image
4. Fax coversheet
5. Shipping label, with our return address and a mail-to address (on one label)

We need these to be editable. We don't know the industry standard for these items but perhaps you can provide them to us in .PDF and Word format (and if you use Adobe Illustrator for them, .AI as well).

Please use the attached placeholder logo in your design entry. We will provide you with the original logo to swap in (same size and design, just different text) when we choose your entry.

Please include the following information on the letterhead and business cards:

58 Birchwell Road
Suite 2B West
New York, NY 10587

Tel: 555-014-2837
Fax :555-014-2837

Please contact us if you have any questions about this contest.

Hi,

Thanks for your interest in this project. The logo to use should be working now. Please contact me if you have any further issues or questions.

I look forward to seeing your submissions. 

Hi,

We first wish to thank you all for your submissions. 

Here is some general feedback regarding the designs shown:

1. We would prefer square (as opposed to rounded) business cards.

2. For the fax coversheets, we are looking with a designed look. While we understand these are samples, we don't want it to appear as if it a standard block of text or a fax template from a word processing program.

3. For the 1st page of letterhead and envelopes, we do need an office address on them. The envelopes should have space for a stamp in the top right corner. We would prefer the envelopes not to have colored stripes.

4. We think a watermark of the logo is an interesting idea on the business cards and/or letterhead. This may be something to try. However, it is not strictly necessary and we would like to evaluate designs with and without it.

In general we are looking for a clean yet professional look.

We are actively reviewing all entries and thank you for your time and creativity.

One last comment: We understand making all objects in the brief takes some time. However, we want to remind all the designers that this contest is for more than just business cards (envelopes, letterheads, etc.) so if we choose your design, those items will be expected. Please refer to the original brief to see what we are requesting.

If you provide a mockup of any item listed in the brief (in addition to business cards) it would help us visualize your entire vision for this project.

```html
<!DOCTYPE html>
<html lang="en">
<head>
<meta charset="utf-8">
<title>Halden &amp; Halden — Stationery Set</title>
<link href="https://fonts.googleapis.com/css2?family=Lato:wght@300;400;700&display=swap" rel="stylesheet">
<style>
  :root{
    --bg:#efefef;
    --paper:#f8f8f8;
    --navy:#2b4a66;
    --navy-deep:#1f3348;
    --navy-light:#3b6a91;
    --ink:#4a4a4a;
    --grey:#7a7a7a;
    --window:#dcdcdc;
  }
  *{margin:0;padding:0;box-sizing:border-box}
  html,body{width:1200px;height:924px;overflow:hidden;background:var(--bg);font-family:'Lato',sans-serif;color:var(--ink)}
  .canvas{position:relative;width:1200px;height:924px}
  .sheet{position:absolute;background:var(--paper)}

  .brand{position:absolute;display:flex;align-items:center;gap:6px}
  .brand-square{background:var(--navy);flex:none}
  .brand-name{font-weight:300;color:var(--grey);line-height:1.05}

  .contact{position:absolute;font-size:4px;line-height:5.5px;color:var(--grey);display:flex;gap:10px}
  .contact b{font-weight:700;color:var(--ink)}

  /* letterhead */
  .letterhead{left:222px;top:98px;width:355px;height:503px}
  .letterhead .brand{left:34px;top:33px}
  .letterhead .brand-square{width:34px;height:34px}
  .letterhead .brand-name{font-size:17px}
  .letterhead .contact{left:34px;top:80px}
  .salutation{position:absolute;left:34px;top:141px;font-size:8.5px;font-weight:700;color:var(--ink)}
  .body-copy{position:absolute;left:34px;top:160px;width:293px;font-size:5.6px;line-height:8.1px;text-align:justify;color:var(--grey)}
  .body-copy p{margin-bottom:8px}
  .signature{position:absolute;left:192px;top:385px;width:88px;height:42px;background:linear-gradient(135deg,rgba(80,100,190,.12),rgba(80,100,190,.04));border-radius:4px}
  .closing{position:absolute;right:28px;top:390px;text-align:right;font-size:5.5px;color:var(--grey)}
  .closing strong{display:block;margin-top:5px;font-size:7.5px;color:var(--ink)}

  /* folder */
  .folder{left:640px;top:76px;width:420px;height:528px;
    background:linear-gradient(180deg,rgba(255,255,255,0) 0,rgba(255,255,255,0) 100%),
    linear-gradient(160deg,var(--navy-light) 0%,var(--navy) 45%,var(--navy-deep) 100%)}
  .folder-band{position:absolute;left:0;width:100%;border-top:1px solid rgba(255,255,255,.05)}
  .folder-label{position:absolute;left:245px;top:161px;width:175px;height:74px;background:var(--paper)}
  .folder-label .brand{left:19px;top:17px}
  .folder-label .brand-square{width:40px;height:40px}
  .folder-label .brand-name{font-size:19px}

  /* business cards */
  .card{width:159px;height:90px}
  .card-front{left:95px;top:647px}
  .card-front .brand{left:12px;top:13px}
  .card-back{left:95px;top:764px}
  .card-back .brand{left:72px;top:25px}
  .card .brand-square{width:22px;height:22px}
  .card .brand-name{font-size:10px;gap:4px}
  .card-name{position:absolute;font-size:5px;font-weight:700;color:var(--navy)}
  .card-role{position:absolute;font-size:3.6px;color:var(--grey)}
  .card-front .card-name{right:14px;top:55px}
  .card-front .card-role{right:14px;top:61px}
  .card-front .card-line{position:absolute;right:14px;font-size:3.6px;color:var(--grey)}
  .card-back .card-name{left:24px;top:65px}
  .card-back .card-role{left:24px;top:71px}
  .card-back .card-addr{position:absolute;left:24px;top:24px;font-size:3.6px;line-height:4.6px;color:var(--grey)}

  /* window envelope */
  .envelope{left:297px;top:660px;width:397px;height:190px}
  .envelope .window{position:absolute;left:56px;top:107px;width:155px;height:53px;background:var(--window);border-radius:4px}
  .envelope .brand{left:238px;top:114px}
  .envelope .brand-square{width:34px;height:34px}
  .envelope .brand-name{font-size:17px}
  .envelope .contact{left:238px;top:168px}

  /* envelope back */
  .envelope-back{left:733px;top:660px;width:370px;height:190px}
  .envelope-back .flap{position:absolute;left:0;top:0;width:370px;height:68px}
  .flap-mark{position:absolute;left:185px;top:27px;width:18px;height:18px;margin-left:-9px;background:rgba(255,255,255,.18)}
</style>
</head>
<body>
<div class="canvas">

  <section class="sheet letterhead">
    <div class="brand"><span class="brand-square"></span><span class="brand-name">Halden<br>&amp; Halden</span></div>
    <div class="contact">
      <div><b>Tel:</b> 555-014-2837<br><b>Fax:</b> 555-014-2837</div>
      <div>58 Birchwell Road, Suite 2B West<br>New York, NY 10587</div>
    </div>
    <p class="salutation">Dear sir / madame,</p>
    <div class="body-copy">
      <p>Lorem ipsum dolor sit amet, consectetur adipisicing elit, sed do eiusmod tempor incididunt ut labore et dolore magna aliqua. Ut enim ad minim veniam, quis nostrud exercitation ullamco laboris nisi ut aliquip ex ea commodo consequat. Duis aute irure dolor in reprehenderit in voluptate velit esse cillum dolore eu fugiat nulla pariatur. Excepteur sint occaecat cupidatat non proident, sunt in culpa qui officia deserunt mollit anim id est laborum. Lorem ipsum dolor sit amet, consectetur adipisicing elit, sed do eiusmod tempor incididunt ut labore et dolore magna aliqua. Ut enim ad minim veniam, quis nostrud exercitation ullamco laboris nisi ut aliquip ex ea commodo consequat. Duis aute irure dolor in reprehenderit in voluptate velit esse cillum dolore eu fugiat nulla pariatur. Excepteur sint occaecat cupidatat non proident, sunt in culpa qui officia deserunt mollit anim id est laborum.</p>
      <p>Lorem ipsum dolor sit amet, consectetur adipisicing elit, sed do eiusmod tempor incididunt ut labore et dolore magna aliqua. Ut enim ad minim veniam, quis nostrud exercitation ullamco laboris nisi ut aliquip ex ea commodo consequat. Duis aute irure dolor in reprehenderit in voluptate velit esse cillum dolore eu fugiat nulla pariatur. Excepteur sint occaecat cupidatat non proident, sunt in culpa qui officia deserunt mollit anim id est laborum.</p>
      <p>Lorem ipsum dolor sit amet, consectetur adipisicing elit, sed do eiusmod tempor incididunt ut labore et dolore magna aliqua. Ut enim ad minim veniam, quis nostrud exercitation ullamco laboris nisi ut aliquip ex ea commodo consequat. Duis aute irure dolor in reprehenderit in voluptate velit esse cillum dolore eu fugiat nulla pariatur. Excepteur sint occaecat cupidatat non proident, sunt in culpa qui officia deserunt mollit anim id est laborum.</p>
      <p>Lorem ipsum dolor sit amet, consectetur adipisicing elit, sed do eiusmod tempor incididunt ut labore et dolore magna aliqua. Ut enim ad minim veniam, quis nostrud exercitation ullamco laboris nisi ut aliquip ex ea commodo consequat. Duis aute irure dolor in reprehenderit in voluptate velit esse cillum dolore eu fugiat nulla pariatur. Excepteur sint occaecat cupidatat non proident, sunt in culpa qui officia deserunt mollit anim id est laborum.</p>
    </div>
    <div class="signature" role="img" aria-label="Handwritten signature of Lena Corvin"></div>
    <div class="closing">Yours Sincerely,<strong>Lena Corvin</strong></div>
  </section>

  <section class="sheet folder">
    <span class="folder-band" style="top:131px"></span>
    <span class="folder-band" style="top:264px"></span>
    <span class="folder-band" style="top:396px"></span>
    <div class="folder-label">
      <div class="brand"><span class="brand-square"></span><span class="brand-name">Halden<br>&amp; Halden</span></div>
    </div>
  </section>

  <section class="sheet card card-front">
    <div class="brand"><span class="brand-square"></span><span class="brand-name">Halden<br>&amp; Halden</span></div>
    <p class="card-name">OWEN PRUITT</p>
    <p class="card-role">Managing Director</p>
    <p class="card-line" style="top:74px">58 Birchwell Road, Suite 2B West, New York, NY 10587</p>
    <p class="card-line" style="top:79px"><b>Phone:</b> 555-014-2837 &nbsp;<b>Fax:</b> 555-014-2837</p>
  </section>

  <section class="sheet card card-back">
    <p class="card-addr">58 Birchwell Road<br>Suite 2B West<br>New York, NY 10587<br><b>Phone:</b> 555-014-2837<br><b>Fax:</b> 555-014-2837</p>
    <div class="brand"><span class="brand-square"></span><span class="brand-name">Halden<br>&amp; Halden</span></div>
    <p class="card-name">OWEN PRUITT</p>
    <p class="card-role">Managing Director</p>
  </section>

  <section class="sheet envelope">
    <span class="window"></span>
    <div class="brand"><span class="brand-square"></span><span class="brand-name">Halden<br>&amp; Halden</span></div>
    <div class="contact">
      <div><b>Tel:</b> 555-014-2837<br><b>Fax:</b> 555-014-2837</div>
      <div>58 Birchwell Road, Suite 2B West<br>New York, NY 10587</div>
    </div>
  </section>

  <section class="sheet envelope-back">
    <svg class="flap" viewBox="0 0 370 68" aria-hidden="true">
      <path d="M0 0H370V56Q370 62 362 63L12 68Q0 68 0 60Z" fill="var(--navy)"/>
    </svg>
    <span class="flap-mark"></span>
  </section>

</div>
</body>
</html>
```